Corporate Power Point Template

Tarnel Holdings, Inc. produces and sells ready-mixed concrete, aggregates, and concrete-related products and services for the construction industry in the United States.

We are looking for a simple and sleek design that will look great on a projector, as well as when printed on paper. We prefer a lighter background color that will not waste ink when printed. We would also like to stay away from wavy banners, or over-the-top graphics that take away from usable space in the deck. Please use a variation of the color scheme in the "Brand Standards" file attached.

Construction

```html
<!DOCTYPE html>
<html lang="en">
<head>
<meta charset="utf-8">
<title>Tarnel Holdings – Corporate Template</title>
<link href="https://fonts.googleapis.com/css2?family=Open+Sans:wght@400;700&display=swap" rel="stylesheet">
<style>
:root{
  --canvas:#c2c2c2;
  --paper:#ffffff;
  --red:#c8202f;
  --slate:#626264;
  --slate-dark:#4f4f51;
  --ink:#555557;
  --soft:#d9d9d9;
  --pale:#efefef;
}
*{box-sizing:border-box;margin:0;padding:0}
html,body{width:1200px;height:1200px;overflow:hidden;background:var(--canvas);font-family:"Open Sans",Arial,sans-serif;color:var(--ink)}
.slide{position:absolute;background:var(--paper);overflow:hidden}
.abs{position:absolute}
.logo{position:absolute;display:flex;align-items:center;gap:2px;font-weight:700;color:var(--slate);letter-spacing:.3px}
.logo i{display:block;background:var(--red)}
.logo.sm{top:4px;right:8px;font-size:4px}
.logo.sm i{width:3px;height:3px}
.logo.lg{font-size:8px}
.logo.lg i{width:6px;height:6px}
.heading{position:absolute;top:4px;left:0;font-size:6.4px;color:#7a7a7c;padding-left:6px;border-left:2px solid var(--red);line-height:7px}
.footer{position:absolute;left:0;right:0;bottom:0;height:3px;background:var(--slate)}
.footer::after{content:"";position:absolute;right:10px;top:0;width:10px;height:3px;background:var(--red)}
.footer span{position:absolute;left:4px;top:-0.5px;font-size:2px;color:#fff}
.para{position:absolute;font-size:2.6px;line-height:3.4px;color:var(--ink)}
.label{font-size:3px;color:var(--ink);font-weight:700}
.photo{position:absolute}
.icon{position:absolute;border-radius:50%;background:var(--pale);display:flex;align-items:center;justify-content:center}
.icon b{display:block;width:40%;height:40%;border:1px solid var(--red);border-radius:1px}
.avatar{position:absolute;border-radius:50%;background:linear-gradient(#8a6a58,#d9b8a2)}
.cover-band{position:absolute;background:var(--slate);color:#fff;text-align:center;clip-path:polygon(0 0,100% 0,100% 100%,0 78%)}
.cover-block{position:absolute;background:var(--slate-dark)}
.cover-title{font-weight:700;letter-spacing:.6px}
.contact{position:absolute;font-size:2.6px;line-height:3.2px;color:var(--ink)}
.contact div{display:flex;gap:3px;margin-bottom:3px}
.contact i{display:block;width:3px;height:3px;border-radius:50%;background:var(--slate)}
.agenda li{list-style:none;font-size:3.6px;color:#7a7a7c;margin-bottom:11px}
.bar{position:absolute;bottom:0;width:7px}
.bar.r{background:var(--red)}
.bar.g{background:#c7c7c7}
.pct{position:absolute;border-radius:50%;background:var(--slate);color:#fff;font-size:8px;display:flex;align-items:center;justify-content:center}
</style>
</head>
<body>

<!-- Cover -->
<section class="slide" style="left:103px;top:29px;width:204px;height:115px">
  <div class="logo lg" style="left:4px;top:4px"><i></i>TARNEL</div>
  <div class="cover-block" style="left:0;top:53px;width:40px;height:50px"></div>
  <div class="cover-band" style="left:39px;top:40px;width:165px;height:70px">
    <div class="cover-title" style="font-size:7.6px;margin-top:11px">PRESENTATION TITLE</div>
    <div style="font-size:3px;line-height:4px;margin:4px 6px 0">Tarnel Holdings, Inc. produces and sells ready-mixed concrete, aggregates, and concrete-related products and services for the construction industry in the United States.</div>
  </div>
</section>

<!-- Welcome -->
<section class="slide" style="left:318px;top:35px;width:189px;height:107px">
  <div class="logo lg" style="left:4px;top:4px"><i></i>TARNEL</div>
  <div class="abs" style="left:4px;top:28px;font-size:4.4px;color:#7a7a7c">Welcome Message</div>
  <div class="para" style="left:4px;top:37px;width:92px">Tarnel Holdings, Inc. produces and sells ready-mixed concrete, aggregates, and concrete-related products for the construction industry.</div>
  <div class="para" style="left:4px;top:55px;width:92px">We believe strong work begins with clear goals, careful planning and a team that delivers on time. Our crews work across the region to build lasting value for every client we serve.</div>
  <div class="photo" role="img" aria-label="Photo of a modern glass office tower" style="left:122px;top:8px;width:67px;height:96px;background:linear-gradient(135deg,#2f5fa8,#9fb6d4 55%,#5d6f86)"></div>
</section>

<!-- Agenda -->
<section class="slide" style="left:100px;top:158px;width:206px;height:134px">
  <div class="heading">Agenda</div>
  <div class="logo sm"><i></i>TARNEL</div>
  <div class="photo" role="img" aria-label="Photo of concrete mixer trucks at a batching plant" style="left:10px;top:25px;width:74px;height:80px;background:linear-gradient(160deg,#3f6fb5,#7f8c99 50%,#a33a3a)"></div>
  <ul class="agenda abs" style="left:100px;top:24px">
    <li>1.&nbsp;&nbsp;Mission</li><li>2.&nbsp;&nbsp;Today's Situation</li><li>3.&nbsp;&nbsp;Why Invest?</li><li>4.&nbsp;&nbsp;The Key to Success</li><li>5.&nbsp;&nbsp;Why Choose</li><li>6.&nbsp;&nbsp;Our Team</li>
  </ul>
  <div class="footer"><span>Tarnel Holdings</span></div>
</section>

<!-- Profile -->
<section class="slide" style="left:316px;top:158px;width:206px;height:134px">
  <div class="heading">Sample Text</div>
  <div class="logo sm"><i></i>TARNEL</div>
  <div class="avatar" role="img" aria-label="Portrait photo of a team member" style="left:94px;top:22px;width:18px;height:18px"></div>
  <div class="para" style="left:16px;top:51px;width:174px;text-align:center">Tarnel Holdings, Inc. produces and sells ready-mixed concrete, aggregates, and concrete-related products and services for the construction industry.</div>
  <div class="para" style="left:16px;top:62px;width:174px;text-align:center">We are looking for a simple and sleek design that will look great on a projector as well as when printed on paper. We prefer a lighter background that will not waste ink and keeps the usable space open for content.</div>
  <div class="footer"><span>Tarnel Holdings</span></div>
</section>

<!-- Photo left, two items -->
<section class="slide" style="left:102px;top:309px;width:206px;height:132px">
  <div class="heading">Sample Text</div>
  <div class="logo sm"><i></i>TARNEL</div>
  <div class="photo" role="img" aria-label="Photo of a modern office building under blue sky" style="left:11px;top:23px;width:62px;height:90px;background:linear-gradient(170deg,#4d86d1,#c9d8e8 45%,#7d8a8f)"></div>
  <div class="icon" style="left:66px;top:33px;width:12px;height:12px"><b></b></div>
  <div class="icon" style="left:66px;top:74px;width:12px;height:12px"><b></b></div>
  <div class="para" style="left:86px;top:33px;width:112px"><div class="label">Sample Text</div>We deliver quality concrete and aggregates to builders across the region, backed by skilled crews and dependable equipment for every project size.</div>
  <div class="para" style="left:86px;top:74px;width:112px"><div class="label">Sample Text</div>Our plants run on safe, efficient processes so that each load arrives on schedule and meets the standards our clients expect.</div>
  <div class="footer"><span>Tarnel Holdings</span></div>
</section>

<!-- One item, photo right -->
<section class="slide" style="left:319px;top:309px;width:206px;height:134px">
  <div class="heading">Sample Text</div>
  <div class="logo sm"><i></i>TARNEL</div>
  <div class="icon" style="left:10px;top:34px;width:13px;height:13px"><b></b></div>
  <div class="para" style="left:32px;top:36px;width:64px"><div class="label">Sample Text</div>Our teams place forms and pour walls with care, keeping every site clean, safe and on plan from start to finish for each client.</div>
  <div class="photo" role="img" aria-label="Photo of a worker building a block wall" style="left:114px;top:31px;width:81px;height:61px;background:linear-gradient(135deg,#6b6b5a,#b89a7a 60%,#8a7f73)"></div>
  <div class="footer"><span>Tarnel Holdings</span></div>
</section>

<!-- Three columns -->
<section class="slide" style="left:102px;top:456px;width:206px;height:132px">
  <div class="heading">Sample Text</div>
  <div class="logo sm"><i></i>TARNEL</div>
  <div class="icon" style="left:30px;top:25px;width:12px;height:12px"><b></b></div>
  <div class="icon" style="left:87px;top:25px;width:12px;height:12px"><b></b></div>
  <div class="icon" style="left:144px;top:25px;width:12px;height:12px"><b></b></div>
  <div class="para" style="left:14px;top:48px;width:44px;text-align:center"><div class="label">Sample Text</div>Ready-mixed concrete delivered fresh to every job site in the region.</div>
  <div class="para" style="left:71px;top:48px;width:44px;text-align:center"><div class="label">Sample Text</div>Aggregates sourced from our own quarries for steady supply.</div>
  <div class="para" style="left:128px;top:48px;width:44px;text-align:center"><div class="label">Sample Text</div>Related products and services for builders of all sizes.</div>
  <div class="footer"><span>Tarnel Holdings</span></div>
</section>

<!-- Statement -->
<section class="slide" style="left:314px;top:457px;width:205px;height:124px">
  <div class="logo lg" style="left:32px;top:2px"><i></i>TARNEL</div>
  <div class="abs" style="left:8px;top:26px;width:92px;font-size:4.4px;line-height:6px;color:#7a7a7c;text-align:center">XXX Is One Developer Of Class A Office, Industrial And Retail Shopping Centers Throughout The Northwest</div>
  <div class="abs" style="left:106px;top:28px;width:1px;height:44px;background:var(--soft)"></div>
  <div class="para" style="left:97px;top:18px;width:100px">We are looking for a simple and sleek design that will look great on a projector and in print. We prefer a lighter background that saves ink.</div>
  <div class="para" style="left:97px;top:47px;width:100px">We would also like to stay away from wavy banners or busy graphics that take away from the usable space in the deck.</div>
  <div class="footer"><span>Tarnel Holdings</span></div>
</section>

<!-- Photo + two columns -->
<section class="slide" style="left:103px;top:600px;width:205px;height:134px">
  <div class="heading">Sample Text</div>
  <div class="logo sm"><i></i>TARNEL</div>
  <div class="photo" role="img" aria-label="Photo of a worker finishing fresh concrete" style="left:6px;top:27px;width:54px;height:59px;background:linear-gradient(150deg,#7d6a58,#c2b3a2 55%,#a89684)"></div>
  <div class="icon" style="left:87px;top:24px;width:14px;height:14px"><b></b></div>
  <div class="icon" style="left:154px;top:24px;width:14px;height:14px"><b></b></div>
  <div class="para" style="left:70px;top:43px;width:50px"><div class="label" style="text-align:center">Sample Text</div>Our finishing crews level and cure each slab with care so it lasts for years under heavy daily use and changing weather across every season.</div>
  <div class="para" style="left:138px;top:43px;width:50px"><div class="label" style="text-align:center">Sample Text</div>Quality checks at every stage keep our mixes strong and consistent, giving clients confidence in each pour we deliver on site.</div>
  <div class="footer"><span>Tarnel Holdings</span></div>
</section>

<!-- Process -->
<section class="slide" style="left:321px;top:599px;width:206px;height:133px">
  <div class="heading">Sample Text</div>
  <div class="logo sm"><i></i>TARNEL</div>
  <svg class="abs" style="left:18px;top:40px" width="170" height="14" viewBox="0 0 170 14">
    <g fill="#efefef"><circle cx="8" cy="7" r="7"/><circle cx="56" cy="7" r="7"/><circle cx="104" cy="7" r="7"/><circle cx="152" cy="7" r="7"/></g>
    <g fill="none" stroke="#c8202f" stroke-width=".8"><rect x="5" y="4" width="6" height="6"/><rect x="53" y="4" width="6" height="6"/><rect x="101" y="4" width="6" height="6"/><rect x="149" y="4" width="6" height="6"/></g>
    <g fill="#888"><path d="M29 5l3 2-3 2z"/><path d="M77 5l3 2-3 2z"/><path d="M125 5l3 2-3 2z"/></g>
  </svg>
  <div class="para" style="left:16px;top:76px;width:174px;text-align:center">We are looking for a simple and sleek design that will look great on a projector and when printed on paper. We prefer a lighter background color that will not waste ink, keeping every step of the process clear for the reader.</div>
  <div class="footer"><span>Tarnel Holdings</span></div>
</section>

<!-- Team -->
<section class="slide" style="left:104px;top:747px;width:205px;height:136px">
  <div class="heading">Sample Text</div>
  <div class="logo sm"><i></i>TARNEL</div>
  <div class="para" style="left:10px;top:24px;width:50px;text-align:center">Team Lead</div>
  <div class="para" style="left:78px;top:24px;width:50px;text-align:center">Sales Director</div>
  <div class="para" style="left:144px;top:22px;width:50px;text-align:center">Regional Operations Manager</div>
  <div class="avatar" role="img" aria-label="Portrait photo of a team member" style="left:17px;top:35px;width:20px;height:20px"></div>
  <div class="avatar" role="img" aria-label="Portrait photo of a team member" style="left:89px;top:35px;width:20px;height:20px"></div>
  <div class="avatar" role="img" aria-label="Portrait photo of a team member" style="left:154px;top:35px;width:20px;height:20px"></div>
  <div class="para" style="left:10px;top:61px;width:52px">Leads planning and crews on large builds across the region.</div>
  <div class="para" style="left:80px;top:61px;width:52px">Builds lasting ties with contractors and new clients.</div>
  <div class="para" style="left:146px;top:61px;width:52px">Runs plant output and delivery for every district.</div>
  <div class="footer"><span>Tarnel Holdings</span></div>
</section>

<!-- Percentages -->
<section class="slide" style="left:321px;top:747px;width:205px;height:134px">
  <div class="heading">Sample Text</div>
  <div class="logo sm"><i></i>TARNEL</div>
  <div class="icon" style="left:26px;top:38px;width:20px;height:20px"><b></b></div>
  <div class="pct" style="left:46px;top:26px;width:18px;height:18px">76%</div>
  <div class="icon" style="left:117px;top:38px;width:20px;height:20px"><b></b></div>
  <div class="pct" style="left:136px;top:26px;width:18px;height:18px">68%</div>
  <div class="para" style="left:16px;top:70px;width:70px;text-align:center">Share of projects finished ahead of schedule last year, thanks to careful planning and reliable delivery across all sites.</div>
  <div class="para" style="left:110px;top:70px;width:70px;text-align:center">Share of repeat clients who return to us for new builds, showing trust earned through steady quality and service.</div>
  <div class="footer"><span>Tarnel Holdings</span></div>
</section>

<!-- Chart -->
<section class="slide" style="left:106px;top:894px;width:206px;height:134px">
  <div class="heading">Sample Text</div>
  <div class="logo sm"><i></i>TARNEL</div>
  <div class="abs" style="left:38px;top:32px;width:130px;height:45px;border-left:.5px solid #aaa;border-bottom:.5px solid #aaa">
    <div class="bar r" style="left:8px;height:38px"></div><div class="bar g" style="left:16px;height:11px"></div>
    <div class="bar r" style="left:34px;height:30px"></div><div class="bar g" style="left:42px;height:20px"></div>
    <div class="bar r" style="left:60px;height:26px"></div><div class="bar g" style="left:68px;height:31px"></div>
    <div class="bar r" style="left:86px;height:28px"></div><div class="bar g" style="left:94px;height:26px"></div>
    <div class="bar r" style="left:112px;height:32px"></div><div class="bar g" style="left:120px;height:27px"></div>
  </div>
  <div class="para" style="left:16px;top:93px;width:174px;text-align:center">We are looking for a simple and sleek design that will look great on a projector and when printed. Sales have grown each year as new plants came online and more clients chose our mixes for their builds.</div>
  <div class="footer"><span>Tarnel Holdings</span></div>
</section>

<!-- Thank you -->
<section class="slide" style="left:316px;top:894px;width:217px;height:132px">
  <div class="logo lg" style="left:12px;top:16px"><i></i>TARNEL</div>
  <div class="contact" style="left:160px;top:13px">
    <div><i></i>48 Quarry Rd.<br>Alden, TX 75001</div>
    <div><i></i>555.014.2290</div>
    <div><i></i>www.tarnelholdings.com</div>
  </div>
  <div class="cover-block" style="left:8px;top:64px;width:52px;height:56px"></div>
  <div class="cover-band" style="left:47px;top:52px;width:170px;height:76px">
    <div class="cover-title" style="font-size:10.5px;margin-top:22px">THANK YOU</div>
  </div>
</section>

<section class="slide" style="left:209px;top:1038px;width:206px;height:115px">
  <div class="logo lg" style="left:6px;top:6px"><i></i>TARNEL</div>
  <div class="contact" style="left:154px;top:2px">
    <div><i></i>48 Quarry Rd.<br>Alden, TX 75001</div>
    <div><i></i>555.014.2290</div>
    <div><i></i>www.tarnelholdings.com</div>
  </div>
  <div class="cover-block" style="left:0;top:52px;width:52px;height:53px"></div>
  <div class="cover-band" style="left:41px;top:40px;width:165px;height:75px">
    <div class="cover-title" style="font-size:10.5px;margin-top:22px">THANK YOU</div>
  </div>
</section>

</body>
</html>
```